Brit Rock covers band "The Tin Kettles" requires poster for Marlowe Lounge Friday March 31st

I want a design for a poster (A3 and A4) and Facebook/Instagram ads.
Primary focus is the band name logo "The Tin Kettles", style as in attached file, followed by tag "Old Skool Brit Rock".
Backdrop to be 60's psychedelic art.
Secondary focus is the venue "The Marlowe Lounge"
Supporting text to include:
- 27 Fenwick Road, Chatswood SYDNEY
- Friday 31st March 2023
- 7:00 pm until late
- Bar sales refreshments
- NO admission fee

```html
<!DOCTYPE html>
<html lang="en">
<head>
<meta charset="utf-8">
<title>The Tin Kettles – Old Skool Brit Rock at The Marlowe Lounge</title>
<link rel="stylesheet" href="https://fonts.googleapis.com/css2?family=Abril+Fatface&family=Alfa+Slab+One&family=Shrikhand&family=Playfair+Display:wght@700&family=Inter:wght@500&display=swap">
<style>
  :root {
    --cream: #f6e7cd;
    --royal: #2e47b5;
    --violet: #6b4c9e;
    --pink: #f07d98;
    --coral: #e4514f;
    --navy: #1d2453;
    --ink: #141414;
    --gold: #f4c23f;
  }
  * { margin: 0; padding: 0; box-sizing: border-box; }
  html, body { width: 849px; height: 1200px; overflow: hidden; background: var(--cream); }
  .poster { position: relative; width: 849px; height: 1200px; background: var(--cream); overflow: hidden; }

  .psychedelic-backdrop {
    position: absolute; left: 34px; top: 28px; width: 781px; height: 1090px;
    border-radius: 42px;
    background:
      radial-gradient(circle at 50% 45%, var(--pink) 0 30%, transparent 46%),
      radial-gradient(circle at 15% 15%, var(--violet) 0 18%, transparent 34%),
      radial-gradient(circle at 85% 20%, var(--violet) 0 16%, transparent 32%),
      radial-gradient(circle at 20% 80%, var(--coral) 0 14%, transparent 30%),
      radial-gradient(circle at 85% 78%, var(--coral) 0 14%, transparent 30%),
      var(--royal);
  }

  .sun-disc {
    position: absolute; left: 155px; top: 225px; width: 540px; height: 540px;
    border-radius: 50%; background: var(--cream);
  }

  .band-name {
    position: absolute; left: 0; top: 0; width: 849px; text-align: center;
    font-family: "Abril Fatface", serif; color: var(--coral);
    text-shadow: 4px 4px 0 var(--navy);
    letter-spacing: 2px; line-height: 1; font-weight: 400;
  }
  .band-name .line-one { display: block; position: absolute; left: 0; width: 100%; top: 330px; font-size: 96px; }
  .band-name .line-two { display: block; position: absolute; left: 0; width: 100%; top: 430px; font-size: 104px; }

  .tagline {
    position: absolute; left: 0; top: 0; width: 849px; text-align: center;
    font-family: "Alfa Slab One", serif; color: var(--navy); line-height: 1;
  }
  .tagline .tag-top { position: absolute; left: 0; width: 100%; top: 548px; font-size: 50px; letter-spacing: 1px; }
  .tagline .tag-bottom { position: absolute; left: 0; width: 100%; top: 602px; font-size: 40px; letter-spacing: 2px; }

  .ribbons { position: absolute; left: 0; top: 0; }

  .venue-name {
    position: absolute; left: 0; top: 688px; width: 849px; text-align: center;
    font-family: "Playfair Display", serif; font-weight: 700; font-size: 32px; color: var(--cream);
  }
  .genre-tag {
    position: absolute; left: 0; top: 750px; width: 849px; text-align: center;
    font-family: "Alfa Slab One", serif; font-size: 24px; letter-spacing: 2px; color: var(--ink);
  }

  .event-details {
    position: absolute; left: 0; top: 0; width: 849px; text-align: center;
    font-family: "Shrikhand", serif; color: var(--gold); line-height: 1;
  }
  .event-details .address { position: absolute; left: 0; width: 100%; top: 826px; font-size: 27px; letter-spacing: 1px; }
  .event-details .when { position: absolute; left: 0; width: 100%; top: 878px; font-size: 30px; }
  .event-details .time { margin-left: 28px; font-size: 25px; }

  .footer-note {
    position: absolute; top: 1134px;
    font-family: "Inter", sans-serif; font-weight: 500; font-size: 15px; color: var(--ink);
  }
  .footer-note.bar { left: 40px; }
  .footer-note.entry { right: 40px; }
</style>
</head>
<body>
<main class="poster">
  <div class="psychedelic-backdrop" role="img" aria-label="1960s psychedelic swirl pattern in royal blue, violet, pink and coral radiating from the centre"></div>
  <div class="sun-disc"></div>

  <h1 class="band-name">
    <span class="line-one">THE TIN</span>
    <span class="line-two">KETTLES</span>
  </h1>

  <p class="tagline">
    <span class="tag-top">OLD SKOOL</span>
    <span class="tag-bottom">BRIT ROCK</span>
  </p>

  <svg class="ribbons" width="849" height="1200" viewBox="0 0 849 1200" aria-hidden="true">
    <path class="venue-ribbon-tail" d="M205,705 L245,700 L245,752 L205,760 L222,732 Z" fill="#000"/>
    <path class="venue-ribbon-tail" d="M644,705 L604,700 L604,752 L644,760 L627,732 Z" fill="#000"/>
    <path class="venue-ribbon" d="M235,690 Q425,660 614,690 L614,742 Q425,712 235,742 Z" fill="var(--ink)"/>
    <path class="genre-ribbon" d="M345,742 L505,742 L495,766 L505,790 L345,790 L355,766 Z" fill="var(--pink)"/>
    <path class="details-band" d="M60,814 Q425,784 790,814 L790,930 Q425,962 60,930 Z" fill="var(--ink)"/>
  </svg>

  <h2 class="venue-name">The Marlowe Lounge</h2>
  <p class="genre-tag">ROCK</p>

  <p class="event-details">
    <span class="address">27 FENWICK ROAD, CHATSWOOD SYDNEY</span>
    <span class="when">Friday 31st March 2023<span class="time">7:00 pm until late</span></span>
  </p>

  <p class="footer-note bar">Bar sales refreshments</p>
  <p class="footer-note entry">NO admission fee</p>
</main>
</body>
</html>
```